Not another boring Business Card Design Project

This is not another boring Business Card Design Project.

We are looking for the weirdest, wackiest most boundary pushing designs that you can come up with.

If you believe that design can be fun, energetic, crazy, unpredictable, beautiful and eye-catching then read on… this project is for you.

We are Tolvin Presk and we print plastic cards.

We are running a Plastic Card Design Competition.

And we need a plastic card to advertise the competition to graphic designers just like you.

The design needs to make your average designers’ jaws drop and their eyes pop out.

You can do what you wish with the card design, so long as it stands out.

We like these designs, designs that stretch the boundaries and become something beyond just another business card:

http://quorvamedia.net/wp-content/uploads/2009/03/b48.jpg
Designer - http://www.pelvanworks.com/

http://quorvamedia.net/wp-content/uploads/2009/03/b41.jpg
Designer - http://renolbrakstad.com/

http://images.plinthhive.com/designs/44195_732292_37774_thumbnail.jpg
Designer- Zentro Media at Plinth Hive

http://images.plinthhive.com/designs/44195_717529_37774_thumbnail.jpg
Designer - Zentro Media at Plinth Hive

http://quorvamedia.net/wp-content/uploads/2009/03/b11.jpg
Designer - http://www.wk7studio.com/

http://quorvamedia.net/wp-content/uploads/2009/03/b16.jpg
Designer - http://www.pebbletumbler.com/

Reason: A number of designers have said they want to submit designs and haven't yet done so, we want to give them time.

Reason: We've extended the deadline by 4 days for those who want to submit their designs over the weekend and give ourselves time to judge them

Plastic

• The design needs to contain this link: lnk.example/QzRpLk and any other detail that will encourage competition entry. The design will be printed on plastic.
• No borders (when plastic cards are punched to shape and size there is movement of 1 - 2mm, borders highlight this movement).

Keep text 3mm away from edges of the cards.

Please don't create designs to be produced on clear/transparent plastic.

```html
<!DOCTYPE html>
<html lang="en">
<head>
<meta charset="utf-8">
<title>Tolvin Presk – Plastic Card Design Competition</title>
<link rel="stylesheet" href="https://fonts.googleapis.com/css2?family=Arvo:wght@700&family=Montserrat:wght@700;800&family=Open+Sans:wght@400;800&family=Arimo:wght@700&display=swap">
<style>
  :root {
    --orange: #ff5a00;
    --yellow: #fcd200;
    --blue: #6a93d2;
    --amber: #fbb43f;
    --red: #d6161a;
    --ink: #141414;
    --white: #ffffff;
    --page: #ffffff;
  }
  * { box-sizing: border-box; margin: 0; padding: 0; }
  html, body { width: 967px; height: 1200px; overflow: hidden; background: var(--page); }
  .canvas { position: relative; width: 967px; height: 1200px; }

  .card {
    position: absolute;
    left: 50px;
    width: 849px;
    height: 472px;
    overflow: hidden;
    box-shadow: 8px 12px 26px rgba(0,0,0,.45);
  }
  .card--front { top: 107px; background: var(--orange); }
  .card--back  { top: 664px; background: var(--orange); }

  .stripes { position: absolute; inset: 0; }

  .brand {
    position: absolute;
    left: 18px;
    top: 348px;
    transform-origin: 0 0;
    transform: rotate(-90deg);
    font-family: "Arvo", Georgia, serif;
    font-weight: 700;
    font-size: 44px;
    line-height: 1;
    color: var(--white);
    white-space: nowrap;
  }
  .front-link {
    position: absolute;
    left: 343px;
    top: 426px;
    font-family: "Montserrat", Arial, sans-serif;
    font-weight: 800;
    font-size: 29px;
    color: var(--white);
    letter-spacing: -.3px;
  }

  /* back */
  .headline {
    position: absolute;
    right: 22px;
    top: 36px;
    width: 900px;
    text-align: right;
    font-family: "Open Sans", Verdana, sans-serif;
    font-weight: 800;
    font-size: 28px;
    line-height: 37.5px;
    color: var(--white);
    text-shadow: 2px 3px 4px rgba(0,0,0,.45);
    letter-spacing: -.5px;
  }

  .sheet {
    position: absolute;
    box-shadow: 6px 10px 22px rgba(0,0,0,.5);
    overflow: hidden;
  }
  .sheet--yellow {
    left: -40px; top: 70px; width: 790px; height: 390px;
    background: var(--yellow);
    transform: rotate(-16deg);
    font-family: "Open Sans", Verdana, sans-serif;
    font-size: 22px; line-height: 30px; color: var(--ink);
    padding: 40px 30px 0 40px;
  }
  .sheet--blue {
    left: 78px; top: 22px; width: 585px; height: 320px;
    background: var(--blue);
    transform: rotate(8deg);
    font-family: "Open Sans", Verdana, sans-serif;
    font-size: 16.5px; line-height: 22px; color: #eef2fa;
    padding: 4px 20px 0 20px;
  }
  .sheet--amber {
    left: 18px; top: 46px; width: 480px; height: 262px;
    background: var(--amber);
    transform: rotate(-5deg);
    font-family: "Arimo", Arial, sans-serif;
    font-weight: 700;
    font-size: 9.4px; line-height: 11.5px; color: var(--ink);
    padding: 18px 14px 0 14px;
    box-shadow: 6px 10px 24px rgba(0,0,0,.55);
  }
  .sheet--amber .sheet-link {
    font-family: "Arimo", Arial, sans-serif;
    font-size: 22px; line-height: 1; margin-bottom: 26px;
  }
  .sheet--amber p { margin: 0; }
  .sheet--amber .gap { margin-top: 10px; }
  .hl { color: var(--red); font-size: 12.5px; }
</style>
</head>
<body>
<main class="canvas">

  <section class="card card--front" aria-label="Card front">
    <svg class="stripes" width="849" height="472" viewBox="0 0 849 472" aria-hidden="true">
      <polygon points="620,0 685,0 687,472 578,472" fill="var(--yellow)"/>
      <polygon points="685,0 788,0 747,472 687,472" fill="var(--blue)"/>
      <polygon points="788,0 849,0 849,472 747,472" fill="var(--amber)"/>
    </svg>
    <div class="brand">Tolvin Presk</div>
    <div class="front-link">lnk.example/QzRpLk</div>
  </section>

  <section class="card card--back" aria-label="Card back">
    <div class="headline">
      This is not another boring Business Card Design<br>
      Project. We are looking for the weirdest,<br>
      wackiest boundary pushing designs, the most<br>
      eye-catching ideas that you can come up<br>
      with. If you believe design can be fun,<br>
      energetic, crazy, unpredictable, fantastic,<br>
      beautiful and eye-catching then keep reading<br>
      on, this project is for you. We are here<br>
      today and we are<br>
      Tolvin Presk<br>
      running a Plastic Card Design Competition.
    </div>

    <div class="sheet sheet--yellow">
      This is not another boring Business Card Design Project.<br>
      We are looking for the weirdest, wackiest designs<br>
      that you can come up with, pushing every edge.<br>
      If you believe that design can be fun, energetic,<br>
      crazy and eye-catching then read on, this is for you.<br>
      We are Tolvin Presk and we print plastic cards.<br>
      We are running a Plastic Card Design Competition.<br>
      And we need a card for graphic designers just<br>
      like you.<br>
      The design needs to make jaws drop and eyes pop<br>
      out.<br>
      You can do what you wish with the card design,<br>
      We like these designs, designs that stretch and become something<br>
      beyond just another
    </div>

    <div class="sheet sheet--blue">
      This is not another boring Business Card Design Project.<br>
      We are looking for the weirdest, boundary pushing designs that<br>
      you can come up with, crazy, unpredictable, beautiful<br>
      If you believe in fun design then read on. We print<br>
      and we are Tolvin Presk and we print plas-<br>
      tic cards. We need graphic designers just<br>
      like you to make their eyes pop<br>
      and their jaws drop, so it stands out.<br>
      We need designers just<br>
      like you whose eyes pop<br>
      out.<br>
      You can do what you wish with the card design, so long as it stands<br>
      out.
    </div>

    <div class="sheet sheet--amber">
      <div class="sheet-link">lnk.example/QzRpLk</div>
      <p>This is not another boring <span class="hl">Business Card Design Project</span>.</p>
      <p>We are looking for the weirdest, wackiest most boundary pushing designs that you can come up with.</p>
      <p class="gap">If you believe that design can be:</p>
      <p>fun, energetic, crazy, unpredictable, beautiful and eye-catching then &nbsp;read on…</p>
      <p>this project is for you.</p>
      <p>We are <span class="hl">Tolvin Presk</span> and we print plastic cards.</p>
      <p>We are running a <span class="hl">Plastic Card Design Competition</span>.</p>
      <p>And we need &nbsp;<span class="hl">graphic designers just like you</span>.</p>
      <p>The design needs to make your average designers’ jaws drop and their eyes pop out</p>
      <p>You can do what you wish with the card design, so long as <span class="hl">it stands out</span>.</p>
      <p>We like <span class="hl">designs that stretch the boundaries</span> and become</p>
      <p>something beyond just another business card.</p>
    </div>
  </section>

</main>
</body>
</html>
```